PLUMBER,DRAINER,GASFITTER/LPG
blocked drains
new installations
maintenance
stormwater
gutters
all plumbing requirements
no job to small
HONEST RELIABLE FAIR
HI I'm after a professional flyer something that grabs the eye with all the above information in point form, i want to offer free quotes aswell.!
i want my email on there .... tradesbelvine.com
also i want have ...... 24 hour emergency service on there in red and
my lic no 482091k.
and I'm on Facebook under MOSSGATE PLUMBING aswell.
any other information needed its on my website as above
i like the colours black and blue as in photo uploaded .
but very open to anything that you think could be good,

```html
<!DOCTYPE html>
<html lang="en">
<head>
<meta charset="utf-8">
<title>Mossgate Plumbing Flyer</title>
<link href="https://fonts.googleapis.com/css2?family=Montserrat:wght@400;500;600;700;800;900&family=Lobster&display=swap" rel="stylesheet">
<style>
:root{
  --blue:#29a8e0;
  --blue-deep:#1b8ccc;
  --ink:#141414;
  --black:#1c1c1c;
  --red:#e3262b;
  --white:#ffffff;
  --text-light:#e8e8e8;
}
*{box-sizing:border-box;margin:0;padding:0}
html,body{width:927px;height:1200px;overflow:hidden;background:#fff}
.flyer{position:relative;width:927px;height:1200px;overflow:hidden;background:var(--white);font-family:'Montserrat',sans-serif}
.hero-photo{position:absolute;left:420px;top:0;width:507px;height:700px;
  background:linear-gradient(90deg,rgba(255,255,255,1) 0%,rgba(190,200,240,.6) 25%,rgba(120,130,220,.85) 55%,#4656b8 100%),
  linear-gradient(180deg,#6f7fd8 0%,#8c8fe0 40%,#5a67c4 100%)}
.waves{position:absolute;left:0;top:0}
.brand{position:absolute;left:30px;top:60px;width:370px;text-align:center;color:var(--blue)}
.brand-dot{width:54px;height:54px;border-radius:50%;background:var(--blue);margin:0 auto 16px}
.brand-name{font-weight:600;font-size:38px;letter-spacing:1px;line-height:1}
.brand-sub{font-weight:600;font-size:19px;letter-spacing:2px;margin-top:4px}
.tagline-box{position:absolute;left:41px;top:225px;width:363px;height:191px;border:2px solid var(--blue);border-bottom:none;text-align:center}
.tagline-box .title{position:absolute;left:30px;right:30px;top:-12px;background:#fff;color:var(--blue-deep);font-weight:900;font-size:36px;line-height:1}
.tagline-box .subtitle{position:absolute;left:0;right:0;top:26px;color:var(--ink);font-weight:600;font-size:23px}
.tagline-box .script{position:absolute;left:0;right:0;top:58px;color:var(--blue-deep);font-family:'Lobster',cursive;font-size:44px}
.values{position:absolute;left:0;right:0;bottom:0;height:76px;background:var(--blue);color:#fff;font-weight:900;font-size:33px;line-height:34px;padding-top:5px}
.badge{position:absolute;left:96px;top:430px;width:250px;height:250px;border-radius:50%;border:9px solid var(--blue);background:#fff;overflow:hidden;box-shadow:0 4px 10px rgba(0,0,0,.35)}
.badge-inner{position:absolute;inset:0;transform:rotate(-18deg)}
.badge .hrs{position:absolute;left:22px;top:28px;color:var(--red);font-weight:900;font-size:66px;line-height:1}
.badge .hours{position:absolute;left:88px;top:94px;color:var(--red);font-weight:800;font-size:24px}
.badge .emergency{position:absolute;left:8px;top:122px;width:230px;text-align:center;color:var(--ink);font-weight:900;font-size:30px;line-height:30px}
.badge .lic{position:absolute;left:-30px;top:186px;width:320px;height:60px;background:var(--red);color:#fff;font-weight:700;font-size:14px;text-align:center;padding-top:8px}
.worker-photo{position:absolute;left:496px;top:603px;width:431px;height:486px;
  background:radial-gradient(ellipse at 55% 45%,#2d4a86 0%,#1e3566 45%,rgba(28,28,28,0) 75%)}
.about{position:absolute;left:46px;top:698px;width:460px;color:var(--text-light)}
.about h2{color:var(--blue);font-weight:800;font-size:34px;line-height:1.1}
.about p{font-size:19px;line-height:26px;margin-top:4px}
.services-pill{position:absolute;left:0;top:831px;width:254px;height:40px;background:var(--blue);border-radius:0 22px 22px 0;color:#fff;font-size:26px;padding-left:44px;line-height:40px}
.services-pill strong{font-weight:800}
.trades{position:absolute;left:44px;top:888px;color:var(--blue);font-weight:800;font-size:24px;line-height:32px}
.service-list{position:absolute;top:962px;list-style:none;color:#fff;font-weight:600;font-size:19px}
.service-list li{display:flex;align-items:flex-start;height:34px;line-height:24px}
.service-list svg{flex:none;margin:2px 14px 0 0}
.col-a{left:48px}.col-b{left:290px}
.footer-left{position:absolute;left:0;top:1089px;width:400px;height:111px;background:#fff}
.quote-label{position:absolute;left:55px;top:8px;color:var(--blue);font-weight:800;font-size:16px}
.email{position:absolute;left:22px;top:32px;display:flex;align-items:center;gap:8px;font-size:16px;color:var(--ink)}
.follow{position:absolute;left:22px;top:66px;display:flex;align-items:center;gap:8px}
.follow .square{width:28px;height:28px;background:#3b5998}
.follow .label{color:var(--blue);font-weight:800;font-size:12px;line-height:14px}
.follow .name{color:var(--ink);font-weight:500;font-size:13px;line-height:16px}
.footer-right{position:absolute;left:0;top:1089px;width:927px;height:111px}
.phone{position:absolute;left:400px;top:1094px;display:flex;align-items:center;gap:10px;color:#fff;font-weight:900;font-size:50px;line-height:60px}
.web{position:absolute;left:405px;top:1152px;display:flex;align-items:center;gap:12px;color:var(--ink);font-weight:700;font-size:27px}
</style>
</head>
<body>
<main class="flyer">
  <div class="hero-photo" role="img" aria-label="Photo of water cascading from stone wall spouts into a pool"></div>

  <svg class="waves" width="927" height="1200" viewBox="0 0 927 1200" aria-hidden="true">
    <path d="M0,585 C150,520 290,540 420,590 C560,645 720,670 927,575 L927,1089 L0,1089 Z" fill="var(--blue)"/>
    <path d="M0,605 C150,545 290,565 420,615 C560,670 720,700 927,630 L927,1089 L0,1089 Z" fill="var(--black)"/>
    <path d="M380,1089 L927,1089 L927,1200 L345,1200 Z" fill="var(--ink)"/>
    <path d="M400,1089 L927,1089 L927,1200 L370,1200 Z" fill="var(--blue)"/>
  </svg>

  <div class="worker-photo" role="img" aria-label="Photo of a smiling plumber in navy uniform and cap holding a red pipe wrench, giving a thumbs up"></div>

  <header class="brand">
    <div class="brand-dot"></div>
    <div class="brand-name">MOSSGATE</div>
    <div class="brand-sub">PLUMBING</div>
  </header>

  <section class="tagline-box">
    <div class="title">MOSSGATE</div>
    <div class="subtitle">Plumbing Service</div>
    <div class="script">No job to small</div>
    <div class="values">HONEST<br>RELIABLE FAIR</div>
  </section>

  <div class="badge">
    <div class="badge-inner">
      <div class="hrs">24/7</div>
      <div class="hours">HOURS</div>
      <div class="emergency">EMERGENCY<br>SERVICE</div>
      <div class="lic">LIC NO. 482091K</div>
    </div>
  </div>

  <section class="about">
    <h2>Mossgate Plumbing</h2>
    <p>is focused on providing a high-quality service and customer satisfaction; I will do everything I can to meet your plumbing requirements.</p>
  </section>

  <div class="services-pill">Our <strong>Services</strong></div>
  <div class="trades">PLUMBER, DRAINER<br>GASFITTER/LPG</div>

  <ul class="service-list col-a">
    <li><svg width="20" height="20" viewBox="0 0 20 20"><rect x="1" y="3" width="16" height="16" fill="none" stroke="var(--blue)" stroke-width="2"/><path d="M4,10 L8,15 L18,2" fill="none" stroke="var(--blue)" stroke-width="2.4"/></svg>Blocked Drains</li>
    <li><svg width="20" height="20" viewBox="0 0 20 20"><rect x="1" y="3" width="16" height="16" fill="none" stroke="var(--blue)" stroke-width="2"/><path d="M4,10 L8,15 L18,2" fill="none" stroke="var(--blue)" stroke-width="2.4"/></svg>New Installations</li>
    <li><svg width="20" height="20" viewBox="0 0 20 20"><rect x="1" y="3" width="16" height="16" fill="none" stroke="var(--blue)" stroke-width="2"/><path d="M4,10 L8,15 L18,2" fill="none" stroke="var(--blue)" stroke-width="2.4"/></svg>Maintenance</li>
  </ul>
  <ul class="service-list col-b">
    <li><svg width="20" height="20" viewBox="0 0 20 20"><rect x="1" y="3" width="16" height="16" fill="none" stroke="var(--blue)" stroke-width="2"/><path d="M4,10 L8,15 L18,2" fill="none" stroke="var(--blue)" stroke-width="2.4"/></svg>Stormwater</li>
    <li><svg width="20" height="20" viewBox="0 0 20 20"><rect x="1" y="3" width="16" height="16" fill="none" stroke="var(--blue)" stroke-width="2"/><path d="M4,10 L8,15 L18,2" fill="none" stroke="var(--blue)" stroke-width="2.4"/></svg>Gutters</li>
    <li><svg width="20" height="20" viewBox="0 0 20 20"><rect x="1" y="3" width="16" height="16" fill="none" stroke="var(--blue)" stroke-width="2"/><path d="M4,10 L8,15 L18,2" fill="none" stroke="var(--blue)" stroke-width="2.4"/></svg><span>All Plumbing<br>Requirements</span></li>
  </ul>

  <footer>
    <div class="footer-left">
      <div class="quote-label">FOR FREE QUOTATION :</div>
      <div class="email">
        <svg width="22" height="22" viewBox="0 0 22 22"><circle cx="11" cy="11" r="11" fill="var(--blue)"/><rect x="5" y="7" width="12" height="8" fill="none" stroke="#fff" stroke-width="1.5"/><path d="M5,7 L11,12 L17,7" fill="none" stroke="#fff" stroke-width="1.5"/></svg>
        quotes@tradesbelvine.com
      </div>
      <div class="follow">
        <div class="square"></div>
        <div><div class="label">FOLLOW US :</div><div class="name">MOSSGATE PLUMBING</div></div>
      </div>
    </div>
    <div class="phone">
      <svg width="34" height="34" viewBox="0 0 34 34"><circle cx="17" cy="17" r="16" fill="#fff"/><path d="M12,8 C9,12 9,22 12,26 L15,24 L13,19 L15,17 L13,12 L15,10 Z" fill="var(--blue)"/></svg>
      +61 431 572 818
    </div>
    <div class="web">
      <svg width="28" height="28" viewBox="0 0 28 28"><circle cx="14" cy="14" r="13" fill="#fff"/><circle cx="14" cy="14" r="8" fill="none" stroke="var(--blue)" stroke-width="1.6"/><ellipse cx="14" cy="14" rx="3.5" ry="8" fill="none" stroke="var(--blue)" stroke-width="1.4"/><path d="M6,14 H22 M7.5,10 H20.5 M7.5,18 H20.5" stroke="var(--blue)" stroke-width="1.2"/></svg>
      www.tradesbelvine.com.au
    </div>
  </footer>
</main>
</body>
</html>
```